Boracay Wedding Invitation Design

Hello, We would like a wedding invitation design for our wedding in Boracay. We would like it somewhat in the form of a boarding pass with beachy fresh colours, possibly a nice Boracay beach in the background Double sided with an envelope design to match. Maybe something simple on the envelope like a nice picture in the bottom left corner of a shell on a beach or something similar.

I would also like on the opposite side of the invite to be an "information sheet" with a matching beach design

The text files for both sides are included and i have also included 2 designs that i thought looked nice and are similar to what we are after.
Updates

Hello, I have updated the brief to be more specific with text files and images to make it easier for you. Thank you :)

Industry/Entity Type

Wedding

Font styles to use
Decorative
Script

Colors
fbee3d
33a6d7
33b8a4
fbf289
85cae6
ffffff

Requirements
Must have
• I would like to have this quote somewhere on the invitation
• This day I will marry my best friend,
• the one I laugh with,
• live for,
• dream with,
• love
• Owen & Marisa
• Request the pleasure of your company to celebrate their wedding
• On Friday the 17th March 2017
• at
• Velora Grand Suites
• Boracay, Philippines
• Ceremony begins at 3.00pm
• RSVP
• Owen 0437291856
• Marisa 0418273940
• by
• 17th Jan 2016
• Dress: Beach Formal
• For the "information sheet"
• There will be a 5% discount on rooms booked at the Velora under the event Owen & Marisa Wedding. The resort has a total of 24 rooms it would be nice if the majority of guests could stay at the resort from the night before until the night after the wedding but if you choose to stay elsewhere on the island there are plenty of other places to stay for cheaper and everything is fairly close as its a small island.
• We have currently blocked room stay for a short period of time so our guests can book rooms. If you choose to do so please email reservations@veloraresorts-example.com. Once rooms become available to the public again, towards the end of Jan, it will be first come first served basis. The resort is very popular so im assuming once this happens the rooms will be booked out.
• If you would like to check out the resort itself the website is www.veloragrand-example.com
• We know its a fair distance to travel but we would really love to see you all there to celebrate and maybe even enjoy a small holiday while your here its a beautiful part of the world.
• If anyone has any questions please feel free to contact Owen on 0437291856
Nice to have
• A nice picture of a Boracay beach in the background would be nice

```html
<!DOCTYPE html>
<html lang="en">
<head>
<meta charset="utf-8">
<title>Owen &amp; Marisa – Boarding Pass Wedding Invitation</title>
<link href="https://fonts.googleapis.com/css2?family=Comfortaa:wght@300;400&family=Great+Vibes&family=Arimo:wght@400;700&display=swap" rel="stylesheet">
<style>
  :root {
    --page: #efe9df;
    --card-edge: #222222;
    --paper: #ffffff;
    --ink-brown: #5a2a16;
    --ink-dark: #1c1c1c;
    --ink-body: #222222;
    --link: #2a6fc4;
    --accent-pink: #d8145a;
    --photo-top: #6f9fe6;
    --photo-mid: #b9d6ee;
    --photo-low: #eef4f2;
    --stub-top: #c9dcc0;
    --stub-low: #f1f4f1;
  }
  * { box-sizing: border-box; margin: 0; padding: 0; }
  html, body { width: 1200px; height: 1050px; overflow: hidden; }
  body { background: var(--page); position: relative; font-family: "Arimo", Arial, sans-serif; }

  .pass { position: absolute; left: 182px; width: 828px; height: 379px; }
  .pass--front { top: 146px; }
  .pass--back { top: 546px; height: 378px; }

  .segment {
    position: absolute; top: 0; height: 100%;
    border: 1.5px solid var(--card-edge); border-radius: 12px; overflow: hidden;
    background: var(--paper);
  }
  .segment--stub { left: 0; width: 62px; }
  .segment--main { left: 64px; width: 553px; }
  .segment--tag { left: 618px; width: 210px; }

  .beach-photo { position: absolute; inset: 0; }
  .beach-photo--main { background: linear-gradient(180deg, var(--photo-top) 0%, var(--photo-mid) 50%, var(--photo-low) 100%); }
  .beach-photo--tag { background: linear-gradient(180deg, var(--photo-top) 0%, var(--photo-mid) 50%, var(--photo-low) 100%); }
  .beach-photo--stub { background: linear-gradient(180deg, var(--stub-top) 0%, var(--stub-low) 100%); }

  .stub-title {
    position: absolute; left: 50%; top: 50%;
    transform: translate(-50%, -50%) rotate(-90deg);
    white-space: nowrap;
    font-family: "Great Vibes", cursive; font-size: 42px; color: var(--ink-brown);
  }

  .invite { position: absolute; inset: 0; color: var(--ink-brown); font-family: "Comfortaa", sans-serif; font-weight: 300; }
  .invite__line {
    position: absolute; left: 0; width: 530px; text-align: center;
    font-size: 16px; line-height: 20px; word-spacing: 3px; white-space: nowrap;
  }
  .invite__names {
    position: absolute; left: 0; width: 530px; top: 82px; text-align: center;
    font-family: "Great Vibes", cursive; font-weight: 400; font-size: 58px; line-height: 70px; white-space: nowrap;
  }

  .date-stamp { position: absolute; left: 422px; top: 235px; width: 114px; height: 114px; }
  .date-stamp text { font-family: "Comfortaa", sans-serif; fill: var(--ink-brown); }

  .boarding { position: absolute; inset: 0; text-align: center; color: var(--ink-dark); }
  .boarding__status { position: absolute; top: 29px; left: 0; width: 100%; font-family: "Arimo", sans-serif; font-weight: 700; font-size: 16px; letter-spacing: .3px; }
  .boarding__seat {
    position: absolute; left: 56px; top: 51px; width: 99px; height: 60px;
    background: var(--paper); border: 1.5px solid var(--ink-dark);
    font-family: "Arimo", sans-serif; font-weight: 700; font-size: 36px; line-height: 58px;
  }
  .boarding__line { position: absolute; left: 0; width: 100%; font-family: "Comfortaa", sans-serif; font-weight: 300; font-size: 16px; line-height: 20px; white-space: nowrap; }

  .info { position: absolute; left: 65px; top: 22px; width: 440px; color: var(--ink-body); font-size: 11.2px; line-height: 14.4px; }
  .info__heading { text-align: center; font-weight: 700; font-size: 13px; line-height: 16px; margin-bottom: 5px; letter-spacing: .2px; }
  .info p { margin-bottom: 14.4px; }
  .info a { color: var(--link); text-decoration: underline; }
  .info a.info__email { white-space: nowrap; }
  .info__contact { text-align: center; }
  .info__contact strong { color: var(--accent-pink); font-weight: 700; }
</style>
</head>
<body>

  <section class="pass pass--front" aria-label="Invitation front">
    <div class="segment segment--stub">
      <div class="beach-photo beach-photo--stub" role="img" aria-label="Faded strip of the palm-lined beach photo"></div>
      <div class="stub-title">Wedding Invitation</div>
    </div>

    <div class="segment segment--main">
      <div class="beach-photo beach-photo--main" role="img" aria-label="Photo of a Boracay beach with leaning palm trees, white sand and turquoise sea"></div>
      <div class="invite">
        <div class="invite__line" style="top:32px">This day I will marry my best friend,</div>
        <div class="invite__line" style="top:56px">the one I laugh with, live for, dream with, love</div>
        <div class="invite__names">Owen &amp; Marisa</div>
        <div class="invite__line" style="top:167px">Request the pleasure of your company to celebrate</div>
        <div class="invite__line" style="top:191px">their wedding</div>
        <div class="invite__line" style="top:215px">On Friday the 17th March 2017</div>
        <div class="invite__line" style="top:239px">at</div>
        <div class="invite__line" style="top:263px">Velora Grand Suites</div>
        <div class="invite__line" style="top:287px">Boracay, Philippines</div>
        <div class="invite__line" style="top:311px">Ceremony begins at 3.00pm</div>

        <svg class="date-stamp" viewBox="0 0 116 116" aria-label="Date stamp: 17th March 2017">
          <circle cx="58" cy="58" r="56" fill="none" stroke="var(--ink-brown)" stroke-width="1"/>
          <circle cx="58" cy="58" r="52" fill="none" stroke="var(--ink-brown)" stroke-width="1"/>
          <g transform="rotate(-28 58 58)">
            <text x="58" y="44" text-anchor="middle" font-size="15">MARCH</text>
            <text x="58" y="74" text-anchor="middle" font-size="30">17<tspan font-size="18" dy="-10">TH</tspan></text>
            <text x="68" y="92" text-anchor="middle" font-size="15">2017</text>
          </g>
        </svg>
      </div>
    </div>

    <div class="segment segment--tag">
      <div class="beach-photo beach-photo--tag" role="img" aria-label="Photo of beach and sea with a seashell on the sand"></div>
      <div class="boarding">
        <div class="boarding__status">CONFIRMED</div>
        <div class="boarding__seat">3A</div>
        <div class="boarding__line" style="top:126px">RSVP</div>
        <div class="boarding__line" style="top:147px">Owen 0437291856</div>
        <div class="boarding__line" style="top:168px">Marisa 0418273940</div>
        <div class="boarding__line" style="top:189px">by</div>
        <div class="boarding__line" style="top:210px">17th Jan 2016</div>
        <div class="boarding__line" style="top:253px">Dress:</div>
        <div class="boarding__line" style="top:274px">Beach Formal</div>
      </div>
    </div>
  </section>

  <section class="pass pass--back" aria-label="Information sheet">
    <div class="segment segment--stub"></div>
    <div class="segment segment--main">
      <div class="info">
        <h2 class="info__heading">INFORMATION</h2>
        <p>There will be a 5% discount on rooms booked at the Velora under the event Owen &amp; Marisa Wedding. The resort has a total of 24 rooms it would be nice if the majority of guests could stay at the resort from the night before until the night after the wedding but if you choose to stay elsewhere on the island there are plenty of other places to stay for cheaper and everything is fairly close as its a small island.</p>
        <p>We have currently blocked room stay for a short period of time so our guests can book rooms. If you choose to do so please email <a class="info__email" href="mailto:reservations@veloraresorts-example.com">reservations@veloraresorts-example.com</a> Once rooms become available to the public again, towards the end of Jan, it will be first come first served basis. The resort is very popular so im assuming once this happens the rooms will be booked out.</p>
        <p>If you would like to check out the resort itself the website is <a href="#">www.veloragrand-example.com</a></p>
        <p>We know its a fair distance to travel but we would really love to see you all there to celebrate and maybe even enjoy a small holiday while your here its a beautiful part of the world.</p>
        <p class="info__contact">If anyone has any questions please feel free to contact <strong>Owen on 0437291856</strong></p>
      </div>
    </div>
    <div class="segment segment--tag"></div>
  </section>

</body>
</html>
```